website for local kavenda practicioner and yoga teacher trainer

The website should function primarily as:
A place where people can discover Kavenda and book sessions.
A central hub connecting all of my work.
A professional home that reflects my personality and approach.
Website design for Liesbet Oonwerk — Kavenda® Structural Integration practitioner, movement educator, yoga teacher and teacher trainer.
A website that can grow with future projects.
The website should feel: Warm, Human, Invitational, Professional, Accessible, Intelligent, Calm, Clear, Playful, Exploratory, Trustworthy
Avoid: New age aesthetics, Mystical clichés, Excessive spirituality, ”Guru" vibes, Overly clinical design, Corporate wellness branding, Busy layouts
Think: modern, grounded, curious and real.
My work combines three interconnected areas:
1.Bodywork: Touch, structure, awareness and one-on-one support.
2. Movement: Yoga, Pilates and embodied movement.
3. Education: Teacher trainings, workshops and continued learning.
Underlying values:
Curiosity over certainty
Possibility over perfection
Complexity without overwhelm
Science and lived experience together
Exploration rather than dogma
Human beings before methods
The primary goal of the website is to introduce people to Kavenda® Structural Integration and make it easy for them to:
Understand what Kavenda is
Discover whether it might be relevant for them
Learn what to expect from a session
Book an appointment
Booking should always feel visible and easy.
Secondary Goal: Present all other aspects of my work in one coherent place:
Yoga classes
Pilates classes
Teacher trainings
Workshops
Retreats
One-on-one movement sessions
Collaborations with studios
Website Structure
1: HOME
1.1.Hero Section: Large welcoming image
1.2 Two Main Pathways
- Bodywork: Kavenda® Structural Integration
- Movement & Education: Yoga, Pilates, trainings, workshops and retreats
- About Preview: Small introduction with portrait. + Button:
Read More
1.3 Current Events / What's Coming Up: Upcoming trainings, workshops and retreats. (This section should be easy to update)
1.4. Contact / Newsletter: Simple contact information
2: Kavenda® Structural Integration
What is Kavenda?
For whom is it?
What does a session look like?
FAQ
Prices
Booking
Future possibility:
Kaven Movement sessions
3: Movement
- Introductory text.
- Studio Classes (link to “my home base” - > local yoga studio)
- One-to-One Sessions: booking option (this is small; not a key aspect I want to promote)
- Workshops/ Retreats / Teacher Trainings => This section should be flexible and easy to update. Visitors should be able to click into specific offerings.
4. Events
Dynamic page for: Teacher trainings, Retreats, Workshops (see section in movement; here more elaborate)
Each event should contain: Image, Short description, Location, Date, Button for more information. (Linking to hosting studio/location)
5. Work With Me
For studios, organisations and teacher training schools.
Examples: Guest teaching, Workshops, Anatomy, Sequencing, Teacher development , Continuing education -> Clear call-to-action.
Call to action!!=> Book a Session
Prominent button in the navigation.
Footer:
- About Me: Longer biography (6th page)
Personal story and background.
- Testimonials (7th page): Separate page containing testimonials from:
Kavenda clients
Students
Teacher trainees
- Contact: 8th page
Visual Direction
Natural textures. Lots of white space.Editorial feeling.Professional photography.Simple navigation.
Less "wellness influencer.” More:Thoughtful, Contemporary, Timeless, Grounded, Human
Photography should show:
Teaching
Hands-on work
Natural movement
Real interaction
Simplicity
Avoid stereotypical yoga imagery and overly spiritual aesthetics.
Keywords
Warm. Curious. Human. Professional. Embodied. Intelligent. Accessible. Playful. Grounded. Exploratory. Real.
Inspiration / Core Message
Helping people feel more at home in their bodies through touch, movement and education.
The website should communicate that these are not separate services, but different expressions of the same intention:
Bodywork • Movement • Education.
Colours:
light orange/beige: e3d5c4
light orange/off white: f9f7f3
gray azure: 556b78
orange: d07b5a
grey orange: c09f80
dark grey: 3e3e3e
dark gray cyan 2f4f4f
gray green colour: a7c4a0
Fonts: Montserrat and Poppins + raleway
In added documents a try out idea of a website + logo. I will mainly use the logo with diffrent colours (image next to text).
My audience consists of people who want to feel more at home in their bodies and who appreciate a thoughtful, grounded and human approach to movement, touch and education. (30-65yo)
wellbeing
5+ page
- montserrat, poppins, raleway

```html
<!DOCTYPE html>
<html lang="en">
<head>
<meta charset="utf-8">
<title>Liesbet Oonwerk — Yoga &amp; Bodywork</title>
<link rel="stylesheet" href="https://fonts.googleapis.com/css2?family=Montserrat:wght@400;500;600;700&family=Poppins:wght@300;400;500&display=swap">
<style>
:root{
  --beige:#e3d5c4;
  --offwhite:#f9f7f3;
  --azure:#556b78;
  --orange:#d07b5a;
  --orange-deep:#cf7556;
  --grey-orange:#c09f80;
  --dark:#3e3e3e;
  --cyan-dark:#2f4f4f;
  --green:#a7c4a0;
  --sand:#f0e8e2;
  --backdrop:#a9a9a9;
  --white:#ffffff;
}
*{box-sizing:border-box;margin:0;padding:0}
html,body{width:1200px;height:2999px;overflow:hidden}
body{background:var(--backdrop);font-family:"Poppins",sans-serif;color:var(--dark);position:relative}
.page{position:absolute;left:99px;top:80px;width:1002px;height:2837px;background:var(--offwhite);overflow:hidden}
.abs{position:absolute}
.eyebrow{font-family:"Poppins",sans-serif;font-size:7px;letter-spacing:1.6px;text-transform:uppercase;font-weight:500}
.btn{position:absolute;display:flex;align-items:center;justify-content:center;border-radius:6px;font-size:9px;font-weight:500;font-family:"Poppins",sans-serif}
.btn-orange{background:var(--orange);color:var(--white)}
.btn-outline{border:1px solid #9a9a9a;color:var(--dark);background:var(--white)}
.photo{position:absolute}

/* nav */
.brand{display:flex;align-items:center;gap:8px;font-family:"Montserrat",sans-serif;font-weight:500;font-size:17px;white-space:nowrap}
.brand-dot{width:18px;height:18px;border-radius:50%;background:var(--orange)}
.nav-links{left:372px;top:34px;display:flex;gap:17px;font-size:8px;font-weight:500;color:var(--dark);white-space:nowrap}

/* hero */
.hero-photo{left:450px;top:120px;width:500px;height:390px;border-radius:32px;background:linear-gradient(150deg,#efebe6 0%,#e2dcd5 50%,#cfc8c1 100%)}
.hero-title{left:123px;top:152px;font-family:"Montserrat",sans-serif;font-size:35px;line-height:36px;font-weight:700;color:var(--cyan-dark);letter-spacing:-0.6px;white-space:nowrap}
.hero-sub{left:122px;top:239px;width:300px;font-size:10.5px;line-height:17px;font-weight:300;color:var(--dark)}

/* pathways */
.path-card{position:absolute;top:549px;width:366px;height:155px;border-radius:24px;color:var(--white);padding:26px 25px}
.path-card .eyebrow{color:rgba(255,255,255,.85)}
.path-card h3{font-family:"Montserrat",sans-serif;font-weight:500;font-size:16px;margin-top:10px}
.path-card p{font-size:8.5px;line-height:13px;font-weight:300;margin-top:12px;opacity:.92;width:320px}
.path-card .more{font-size:8.5px;font-weight:500;margin-top:11px}

/* about */
.about-band{left:0;top:820px;width:1002px;height:551px;background:var(--sand)}
.about-text{left:432px;top:983px;width:400px}
.about-text .eyebrow{color:var(--orange)}
.about-text h2{font-family:"Montserrat",sans-serif;font-weight:500;font-size:25px;color:var(--dark);margin-top:14px}
.about-text h4{font-family:"Montserrat",sans-serif;font-weight:500;font-size:16px;color:var(--orange);margin-top:6px}
.about-text p{font-size:9.5px;line-height:15px;font-weight:300;margin-top:17px}
.about-text p+p{margin-top:10px}

/* events */
.events-head{left:127px;top:1467px;width:520px}
.events-head .eyebrow{color:var(--orange)}
.events-head h2{font-family:"Montserrat",sans-serif;font-weight:500;font-size:25px;color:var(--dark);margin-top:8px;white-space:nowrap}
.events-head p{font-size:9.5px;line-height:15px;font-weight:300;margin-top:12px;width:380px}
.event-photo{position:absolute;width:237px;height:238px;border-radius:18px}
.event-info{position:absolute;width:230px}
.event-info .eyebrow{color:var(--orange);font-size:6.5px}
.event-info h3{font-family:"Montserrat",sans-serif;font-weight:500;font-size:13px;color:var(--dark);margin-top:6px;white-space:nowrap}
.event-info .meta{font-size:6.5px;color:#7a7a7a;margin-top:5px}
.event-info p{font-size:8px;line-height:12.5px;font-weight:300;margin-top:8px;width:195px}
.event-info .more{font-size:8.5px;color:var(--orange);margin-top:11px}
.arrow-btn{position:absolute;width:32px;height:32px;border-radius:50%;display:flex;align-items:center;justify-content:center}

/* newsletter */
.news-band{left:0;top:2105px;width:1002px;height:366px;background:var(--orange-deep)}
.news-photo{left:560px;top:2127px;width:360px;height:322px;border-radius:26px;background:linear-gradient(170deg,#c97255 0%,#a8705e 45%,#6c5d59 100%)}
.news-text{left:121px;top:2163px;width:300px;color:var(--white)}
.news-text .eyebrow{font-size:6.5px}
.news-text h2{font-family:"Montserrat",sans-serif;font-weight:500;font-size:26px;line-height:31.5px;margin-top:13px}
.email-label{left:121px;top:2331px;color:var(--white);font-size:6.5px}
.email-field{left:121px;top:2346px;width:274px;height:36px;background:var(--white);border-radius:5px;display:flex;align-items:center;padding:3px 3px 3px 12px}
.email-field span{flex:1;font-size:9.5px;color:#8a8a8a}
.email-field .subscribe{width:98px;height:30px;background:var(--green);color:var(--white);font-size:9px;display:flex;align-items:center;justify-content:center;border-radius:3px}
.news-note{left:121px;top:2402px;font-size:7px;color:var(--white);white-space:nowrap}

/* footer */
.footer{left:0;top:2573px;width:1002px;height:264px;background:var(--green);color:var(--white)}
.footer .brand{position:absolute;left:123px;top:62px;color:var(--white)}
.footer .brand-dot{background:var(--white)}
.foot-tag{left:123px;top:110px;width:200px;font-size:8px;line-height:14px;font-weight:300}
.social{position:absolute;top:150px;width:21px;height:21px;border-radius:50%;border:1px solid var(--white)}
.foot-col{position:absolute;top:55px;font-size:8px;line-height:21px;font-weight:300}
.foot-col .eyebrow{font-size:6.5px;line-height:14px;margin-bottom:6px}
.foot-rule{left:99px;top:187px;width:803px;height:1px;background:rgba(255,255,255,.45)}
.foot-bottom{top:206px;font-size:7px;font-weight:300;white-space:nowrap}
</style>
</head>
<body>
<div class="page">

  <!-- navigation -->
  <div class="abs brand" style="left:126px;top:30px;color:var(--dark)"><span class="brand-dot"></span>Liesbet Oonwerk</div>
  <nav class="abs nav-links">
    <span>Kavenda®</span><span>Movement</span><span>Events</span><span>Work With Me</span><span>About</span><span>Testimonials</span><span>Contact</span>
  </nav>
  <div class="btn btn-orange" style="left:800px;top:30px;width:79px;height:20px;font-size:7.5px;border-radius:4px">Book a Session</div>

  <!-- hero -->
  <div class="photo hero-photo" role="img" aria-label="Photo of a woman in a flowing backbend stretch on a soft light background"></div>
  <h1 class="abs hero-title">Feel More At<br>Home In Your Body</h1>
  <p class="abs hero-sub">A thoughtful approach to structural integration, movement education, and conscious embodiment.</p>
  <div class="btn btn-orange" style="left:122px;top:295px;width:95px;height:30px">Book a Session</div>
  <div class="btn btn-outline" style="left:228px;top:295px;width:99px;height:30px">Explore Kavenda®</div>

  <!-- pathways -->
  <div class="path-card" style="left:122px;background:var(--green)">
    <div class="eyebrow">Bodywork</div>
    <h3>Kavenda® Structural Integration</h3>
    <p>A systematic approach to organizing your body in gravity, relieving chronic patterns of tension and discomfort.</p>
    <div class="more">Learn more →</div>
  </div>
  <div class="path-card" style="left:513px;background:var(--orange)">
    <div class="eyebrow">Movement &amp; Education</div>
    <h3>Yoga · Pilates · Workshops</h3>
    <p>Cultivate strength, mobility, and deeper somatic awareness through guided movement practices and immersive learning.</p>
    <div class="more">Explore offerings →</div>
  </div>

  <!-- about -->
  <div class="abs about-band"></div>
  <div class="photo" role="img" aria-label="Portrait of Liesbet sitting on grass, hugging her knees" style="left:131px;top:947px;width:260px;height:324px;border-radius:26px;background:linear-gradient(160deg,#e3d9cd 0%,#c9a48f 60%,#c86e5c 100%)"></div>
  <div class="abs about-text">
    <div class="eyebrow">About Liesbet</div>
    <h2>Yoga and Bodywork</h2>
    <h4>For more ease, resilience, and connection</h4>
    <p>Liesbet is a Certified Kavenda® practitioner, movement educator and teacher trainer. Her work lives at the intersection of anatomy, touch and lived experience — quietly rigorous, always human.</p>
    <p>She works one-to-one with clients, teaches movement classes and trains the next generation of yoga and movement professionals across Europe.</p>
  </div>
  <div class="btn btn-orange" style="left:432px;top:1186px;width:96px;height:29px;font-size:8.5px">View More</div>

  <!-- events -->
  <div class="abs events-head">
    <div class="eyebrow">Upcoming</div>
    <h2>Workshops, retreats &amp; trainings</h2>
    <p>Liesbet is a Certified Kavenda® practitioner, movement educator and teacher trainer. Her work lives at the intersection of anatomy, touch and lived experience — quietly rigorous, always human.</p>
  </div>

  <div class="event-photo" role="img" aria-label="Photo of a group of students practising in a sunlit studio" style="left:127px;top:1644px;background:linear-gradient(160deg,#e8dccb 0%,#b99674 55%,#7a6a5c 100%)"></div>
  <div class="event-info" style="left:127px;top:1894px">
    <div class="eyebrow">Workshop</div>
    <h3>The Architecture of Breath</h3>
    <div class="meta">Sat 14 Sep · 10:00–16:00 · Studio Noord, Antwerp</div>
    <p>A one-day exploration of how the diaphragm, ribs and spine cooperate — through anatomy, touch and movement.</p>
    <div class="more">Learn more →</div>
  </div>

  <div class="event-photo" role="img" aria-label="Photo of bare feet walking on a warm wooden floor" style="left:382px;top:1590px;background:linear-gradient(180deg,#cdb8a3 0%,#b98a62 55%,#8e5a32 100%)"></div>
  <div class="event-info" style="left:382px;top:1841px">
    <div class="eyebrow">Retreat</div>
    <h3>Embodied Anatomy</h3>
    <div class="meta">20 – 25 October · Tuscany, Italy</div>
    <p>Six days of slow mornings, deep study and shared meals. For movement teachers and the deeply curious.</p>
    <div class="more">Learn more →</div>
  </div>

  <div class="event-photo" role="img" aria-label="Photo of a bright, empty studio with plants and a rolled mat" style="left:637px;top:1541px;background:linear-gradient(180deg,#f1ece4 0%,#e6dccd 55%,#c8985f 100%)"></div>
  <div class="event-info" style="left:637px;top:1792px">
    <div class="eyebrow">Training</div>
    <h3>Yoga Teacher Training · Module III</h3>
    <div class="meta">Begins 11 January · Hybrid · Brussels + online</div>
    <p>Functional anatomy, biomechanics and the art of teaching real bodies — taught over six weekends.</p>
    <div class="more">Learn more →</div>
  </div>

  <div class="arrow-btn" style="left:849px;top:1928px;background:var(--orange)">
    <svg width="10" height="10" viewBox="0 0 10 10"><path d="M6 2 L3 5 L6 8" fill="none" stroke="#fff" stroke-width="1.2"/></svg>
  </div>
  <div class="arrow-btn" style="left:849px;top:1964px;background:var(--green)">
    <svg width="10" height="10" viewBox="0 0 10 10"><path d="M4 2 L7 5 L4 8" fill="none" stroke="#fff" stroke-width="1.2"/></svg>
  </div>

  <!-- newsletter -->
  <div class="abs news-band"></div>
  <div class="photo news-photo" role="img" aria-label="Photo of a woman balancing in a seated yoga pose with arms outstretched"></div>
  <div class="abs news-text">
    <div class="eyebrow">Letters, occasionally</div>
    <h2>Slow notes on bodies, movement and the practice of paying attention.</h2>
  </div>
  <div class="abs eyebrow email-label">Email</div>
  <div class="abs email-field"><span>you@somewhere.com</span><div class="subscribe">Subscribe</div></div>
  <div class="abs news-note">Two or three letters a year. No funnels, no urgency — just thoughtful writing on the work.</div>

  <!-- footer -->
  <footer class="abs footer">
    <div class="brand"><span class="brand-dot"></span>Liesbet Oonwerk</div>
    <p class="abs foot-tag">Helping you feel more at home in your body through touch, movement and education.</p>
    <span class="social" style="left:122px"></span>
    <span class="social" style="left:152px"></span>
    <div class="foot-col" style="left:513px">
      <div class="eyebrow">Explore</div>
      Kavenda®<br>Movement<br>Events<br>About
    </div>
    <div class="foot-col" style="left:709px">
      <div class="eyebrow">Connect</div>
      Contact<br>Work With Me<br>studio@liesbetoonwerk.com
    </div>
    <div class="abs foot-rule"></div>
    <div class="abs foot-bottom" style="left:123px">© 2026 Liesbet Oonwerk. All rights reserved.</div>
    <div class="abs foot-bottom" style="left:736px">Terms and Conditions</div>
    <div class="abs foot-bottom" style="left:830px">Privacy Policy</div>
  </footer>

</div>
</body>
</html>
```